BRV Core Values & Guiding Principles Visual System

Design a cohesive set of graphics that visually communicate BRV’s Core Values and Guiding Principles. The work includes a large wall sign, posters, simple icons for stickers and hard hats, a standard Guiding Principles graphic, and a clean email signature, all using a consistent, professional style suitable for an industrial environment.

Target Market(s)

This is mostly internal for employees

Industry/Entity Type

Construction

Requirements
Must have
• Edge and a clean but industrial feel
Nice to have
• See attached
Should not have
• Anything outside of the Brand Guide colors

```html
<!DOCTYPE html>
<html lang="en">
<head>
<meta charset="utf-8">
<title>BRV Core Values Poster</title>
<link href="https://fonts.googleapis.com/css2?family=Montserrat:wght@400;500;600;700;800&display=swap" rel="stylesheet">
<style>
:root{
  --red:#e42a24;
  --black:#1b1b1b;
  --ink:#222222;
  --grey:#4a4a4a;
  --light:#f2f2f2;
  --white:#ffffff;
}
*{margin:0;padding:0;box-sizing:border-box}
html,body{width:776px;height:1200px;overflow:hidden;background:var(--white)}
body{font-family:"Montserrat",Arial,sans-serif;color:var(--ink)}
.poster{position:relative;width:776px;height:1200px;overflow:hidden;background:var(--white)}
.shapes{position:absolute;inset:0}
.hero-copy{position:absolute;left:40px;top:318px;width:360px;color:var(--white)}
.hero-title{font-size:27px;font-weight:700;line-height:1.25;letter-spacing:.3px}
.hero-rule{width:100px;height:4px;background:var(--red);margin:14px 0 14px}
.hero-text{font-size:16px;line-height:1.5;font-weight:400}
.brand{position:absolute;left:500px;top:470px;display:flex;align-items:center;gap:12px}
.brand-dot{width:48px;height:48px;border-radius:50%;background:var(--red)}
.brand-name{font-family:"Montserrat",Arial,sans-serif;font-size:44px;font-weight:500;color:var(--grey);letter-spacing:1px}
.pillar-label{position:absolute;top:752px;width:240px;text-align:center;color:var(--white);font-size:14px;font-weight:700}
.culture-heading{position:absolute;left:50px;top:840px;font-size:23px;font-weight:800;color:var(--ink);letter-spacing:.3px}
.culture-heading span{color:var(--red)}
.value{position:absolute;width:270px}
.value-title{font-size:15.5px;font-weight:700;color:var(--ink);margin-bottom:6px}
.value-text{font-size:12px;line-height:1.45;color:var(--grey)}
.contact{position:absolute;left:558px;top:1108px;color:var(--white);font-weight:700}
.contact-label{font-size:26px;line-height:1.15}
.contact-number{font-size:27px;line-height:1.2}
.copyright{position:absolute;left:48px;top:1171px;color:var(--white);font-size:12.5px;font-weight:600}
</style>
</head>
<body>
<main class="poster">
<svg class="shapes" width="776" height="1200" viewBox="0 0 776 1200" xmlns="http://www.w3.org/2000/svg">
  <defs>
    <linearGradient id="siteTone" x1="0" y1="0" x2="1" y2="1">
      <stop offset="0" stop-color="#9a8c7a"/>
      <stop offset=".55" stop-color="#7d6d5c"/>
      <stop offset="1" stop-color="#a89a88"/>
    </linearGradient>
    <linearGradient id="lowerTone" x1="0" y1="0" x2="0" y2="1">
      <stop offset="0" stop-color="#ffffff"/>
      <stop offset="1" stop-color="#eeeeee"/>
    </linearGradient>
  </defs>
  <rect class="hero-photo" x="0" y="0" width="776" height="452" fill="url(#siteTone)" role="img" aria-label="Aerial view of crews on a lift building a large dark steel water tank on a construction site"/>
  <rect x="0" y="452" width="776" height="240" fill="var(--light)"/>
  <polygon points="250,250 305,250 528,428 776,428 776,452 455,452 262,268" fill="var(--red)"/>
  <polygon points="0,268 262,268 455,452 378,522 0,522" fill="var(--black)"/>
  <rect x="0" y="452" width="776" height="0" fill="var(--white)"/>
  <rect x="0" y="688" width="776" height="112" fill="var(--black)"/>
  <rect x="0" y="800" width="776" height="312" fill="url(#lowerTone)"/>

  <g class="pillars">
    <path d="M62,648 A80,80 0 0 1 222,648" fill="none" stroke="var(--red)" stroke-width="8"/>
    <circle cx="142" cy="660" r="78" fill="var(--white)"/>
    <circle cx="142" cy="660" r="74" fill="#8a6a52" role="img" aria-label="Crew member in hard hat and safety vest working at night"/>
    <path d="M314,648 A80,80 0 0 1 474,648" fill="none" stroke="var(--red)" stroke-width="8"/>
    <circle cx="394" cy="660" r="78" fill="var(--white)"/>
    <circle cx="394" cy="660" r="74" fill="#5c5048" role="img" aria-label="Crew installing a blue valve in an excavated trench"/>
    <path d="M552,648 A80,80 0 0 1 712,648" fill="none" stroke="var(--red)" stroke-width="8"/>
    <circle cx="632" cy="660" r="78" fill="var(--white)"/>
    <circle cx="632" cy="660" r="74" fill="#a8acb0" role="img" aria-label="Interior of a pump station with blue valves and grey pipework"/>
  </g>

  <g class="value-icons">
    <circle cx="83" cy="935" r="31" fill="var(--red)"/>
    <circle cx="83" cy="925" r="7" fill="var(--white)"/>
    <path d="M69,948 q14,-18 28,0 z" fill="var(--white)"/>
    <path d="M76,940 l5,5 l9,-10" fill="none" stroke="var(--red)" stroke-width="2.5"/>

    <circle cx="435" cy="935" r="31" fill="var(--black)"/>
    <circle cx="435" cy="935" r="11" fill="none" stroke="var(--white)" stroke-width="5" stroke-dasharray="4 3"/>
    <circle cx="435" cy="935" r="4" fill="var(--white)"/>

    <circle cx="83" cy="1036" r="31" fill="var(--black)"/>
    <path d="M68,1036 l15,-13 l15,13 v14 h-30 z" fill="none" stroke="var(--white)" stroke-width="3"/>
    <circle cx="83" cy="1037" r="4" fill="var(--white)"/>

    <circle cx="435" cy="1036" r="31" fill="var(--red)"/>
    <polygon points="420,1024 436,1036 420,1048" fill="var(--white)"/>
    <polygon points="436,1024 452,1036 436,1048" fill="var(--white)"/>
  </g>

  <g class="footer">
    <rect x="0" y="1112" width="330" height="32" fill="var(--black)"/>
    <polygon points="306,1144 330,1112 352,1112 328,1144" fill="var(--red)"/>
    <polygon points="338,1144 362,1112 384,1112 360,1144" fill="var(--black)"/>
    <polygon points="370,1144 394,1112 416,1112 392,1144" fill="var(--red)"/>
    <polygon points="0,1158 446,1158 470,1200 0,1200" fill="var(--red)"/>
    <polygon points="510,1076 776,1076 776,1200 468,1200 432,1152" fill="var(--black)"/>
    <path d="M507,1124 c-4,4 -3,12 5,21 c9,9 17,10 21,6 l3,-4 l-7,-6 l-4,3 c-4,-2 -9,-7 -11,-11 l3,-4 l-6,-7 z" fill="var(--white)"/>
    <path d="M521,1120 a14,14 0 0 1 14,14 M521,1126 a8,8 0 0 1 8,8" fill="none" stroke="var(--white)" stroke-width="2.2"/>
  </g>
</svg>

<section class="hero-copy">
  <h1 class="hero-title">UNCOMPROMISED<br>SAFETY</h1>
  <div class="hero-rule"></div>
  <p class="hero-text">We champion an unwavering commitment to safety. Protecting people is our top priority always above production, profit, or pressure.</p>
</section>

<div class="brand"><span class="brand-dot"></span><span class="brand-name">BRV</span></div>

<p class="pillar-label" style="left:22px">Guided by Safety</p>
<p class="pillar-label" style="left:274px">Disciplined to Deliver</p>
<p class="pillar-label" style="left:512px">Committed to Quality</p>

<h2 class="culture-heading">BRV’S EXPANDED <span>CULTURE</span></h2>

<div class="value" style="left:127px;top:896px">
  <h3 class="value-title">Relentless Discipline</h3>
  <p class="value-text">We are committed to excellence through consistency, precision, and steadfast refusal to cut</p>
</div>
<div class="value" style="left:472px;top:896px">
  <h3 class="value-title">Embrace the Hard</h3>
  <p class="value-text">We are committed to excellence through consistency, precision, and steadfast refusal to cut</p>
</div>
<div class="value" style="left:127px;top:995px">
  <h3 class="value-title">Own It</h3>
  <p class="value-text">We are committed to excellence through consistency, precision, and steadfast refusal to cut</p>
</div>
<div class="value" style="left:472px;top:995px">
  <h3 class="value-title">Forward Always</h3>
  <p class="value-text">We are committed to excellence through consistency, precision, and steadfast refusal to cut</p>
</div>

<div class="contact">
  <p class="contact-label">Call us at</p>
  <p class="contact-number">555-014-2870</p>
</div>

<p class="copyright">Copyright 2026 - BRV. All Rights Reserved.</p>
</main>
</body>
</html>
```